Lorvant Stationary and Branding Documents

Corporate Identity Branding stationary needed for IT Recruiting Firm.

I already have a Logo, business cards and website. I need to get designs completed for the remaining corporate identity documents.

The documentation should use similar colors as my website and business card. The designs should modern and clean.

http://lorvantsystems.example/

Target Market(s)

Information Technology Industry

Industry/Entity Type

Information Technology

Colors
3377b5
0255a3
fbee3e
f78f20
f37122
33a6d7
000000
0592cd

Requirements
Must have
• Letter Head
• Folder Design
• PowerPoint Design
• Invoice
• Envelope
Nice to have
• Proposal
• Flyer
• Brochure
Should not have
• Logo
• Business Cards
• Website

```html
<!DOCTYPE html>
<html lang="en">
<head>
<meta charset="utf-8">
<title>Lorvant Flyer</title>
<link href="https://fonts.googleapis.com/css2?family=Lato:wght@400;700&family=PT+Sans:wght@400;700&display=swap" rel="stylesheet">
<style>
  :root {
    --blue: #0b55a3;
    --blue-deep: #0d57a4;
    --charcoal: #333333;
    --orange: #f37122;
    --ink: #2b2b2b;
    --paper: #ffffff;
    --backdrop: #cfd0d2;
    --sky-a: #1a2a44;
    --sky-b: #5fa9d6;
  }
  * { box-sizing: border-box; margin: 0; padding: 0; }
  html, body { width: 1200px; height: 1200px; overflow: hidden; background: var(--backdrop); }
  .flyer {
    position: absolute; left: 197px; top: 30px; width: 806px; height: 1140px;
    background: var(--paper); overflow: hidden;
    font-family: "PT Sans", Arial, sans-serif; color: var(--ink);
  }
  .shapes { position: absolute; inset: 0; }
  .abs { position: absolute; }
  .brand { left: 0; width: 806px; top: 258px; text-align: center; }
  .brand-name {
    font-family: "Lato", Arial, sans-serif; font-weight: 700; font-size: 62px;
    color: var(--blue); letter-spacing: 1px; line-height: 1;
    display: inline-flex; align-items: flex-start; gap: 8px;
  }
  .brand-dot { width: 10px; height: 10px; background: var(--orange); margin-top: 6px; }
  .brand-tag {
    margin-top: 10px; font-family: "Lato", Arial, sans-serif; font-size: 16px;
    letter-spacing: 1.5px; color: var(--ink);
  }
  .heading {
    font-family: "Lato", Arial, sans-serif; font-weight: 700; font-size: 25px;
    color: var(--blue); line-height: 30px;
  }
  .lead {
    font-family: "Lato", Arial, sans-serif; font-weight: 700; font-size: 17px;
    color: var(--blue-deep); margin-right: 10px;
  }
  .body { font-size: 16px; line-height: 19.6px; }
  .about { left: 72px; top: 378px; width: 680px; }
  .about .body { margin-top: 2px; }
  .services { left: 72px; top: 525px; width: 690px; }
  .services .body { margin-top: 8px; }
  .services .body + .body { margin-top: 12px; }
  .advantage { left: 72px; top: 705px; width: 340px; }
  .advantage .sub { font-family: "Lato", Arial, sans-serif; font-weight: 700; font-size: 17px; color: var(--blue-deep); margin: 2px 0 0 3px; }
  .ticks { list-style: none; margin: 16px 0 0 6px; }
  .ticks li { font-size: 17px; line-height: 20px; margin-bottom: 11px; display: flex; align-items: center; }
  .ticks li::before {
    content: ""; width: 9px; height: 11px; border-radius: 2px; background: var(--orange);
    margin-right: 13px; flex: none;
  }
  .succeed { left: 470px; top: 705px; width: 290px; }
  .succeed .body { font-size: 16px; letter-spacing: -0.3px; }
  .succeed .heading .inline-body { font-family: "PT Sans", Arial, sans-serif; font-weight: 400; font-size: 16px; color: var(--ink); letter-spacing: -0.3px; margin-left: 10px; }
  .succeed .ticks { margin-top: 14px; margin-left: 2px; }
  .succeed .ticks li { font-size: 16px; margin-bottom: 8px; }
  .contacts {
    left: 40px; top: 1082px; width: 740px; display: flex; align-items: center;
    font-family: "Lato", Arial, sans-serif; font-size: 13px; color: var(--paper);
  }
  .contact { display: flex; align-items: center; gap: 9px; margin-right: 20px; line-height: 16px; }
  .contact svg { flex: none; }
</style>
</head>
<body>
<main class="flyer">
  <svg class="shapes" width="806" height="1140" viewBox="0 0 806 1140">
    <defs>
      <linearGradient id="sky" x1="0" y1="0" x2="1" y2="0.6">
        <stop offset="0" stop-color="var(--sky-a)"/>
        <stop offset="0.5" stop-color="var(--sky-b)"/>
        <stop offset="1" stop-color="#23364f"/>
      </linearGradient>
    </defs>
    <polygon points="0,0 806,0 806,115 0,265" fill="url(#sky)" role="img" aria-label="Photo of a laptop and tablet surrounded by a glowing globe and a network of business people silhouettes"/>
    <polygon points="806,118 806,198 520,228" fill="var(--charcoal)"/>
    <polygon points="0,264 806,177 806,200 0,290" fill="var(--paper)"/>
    <polygon points="0,952 436,992 520,1000 0,1070" fill="var(--charcoal)"/>
    <polygon points="0,1060 806,935 806,1140 0,1140" fill="var(--blue-deep)"/>
  </svg>

  <header class="abs brand">
    <div class="brand-name">lorvant<span class="brand-dot"></span></div>
    <div class="brand-tag">BUSINESS SOLUTION LLC</div>
  </header>

  <section class="abs about">
    <h2 class="heading">ABOUT LORVANT</h2>
    <p class="body">Lorvant is not a standard recruitment firm. We are veteran IT professionals who know the industry and what it takes to succeed. We work with select candidates and provide them with training and an action plan to move up – not just one rung but all the way to your career goals.</p>
  </section>

  <section class="abs services">
    <h2 class="heading">WHAT WE DO</h2>
    <p class="body"><span class="lead">IT RECRUITING</span>Lorvant is the industry’s premier source for Elite IT talent. We choose the best and make them better. And we believe in the personal touch: At Lorvant, you are family.</p>
    <p class="body"><span class="lead">Career Mentoring</span>Lorvant uses scenario-based training to ensure a candidate has the technical skills and the ability to apply those skills in a real-life business environment</p>
  </section>

  <section class="abs advantage">
    <h2 class="heading">THE LORVANT ADVANTAGE</h2>
    <p class="sub">Lorvant is a better path to IT talent</p>
    <ul class="ticks">
      <li>We believe talent is everything</li>
      <li>We’re in it for the long run</li>
      <li>We Live What We do</li>
      <li>We love what we do</li>
    </ul>
  </section>

  <section class="abs succeed">
    <h2 class="heading">LORVANT HELPS SMART COMPANIES SUCCEED FASTER<span class="inline-body">With Lorvant, there’s no</span></h2>
    <p class="body">guesswork or ramp-up: you have a quality candidate uniquely prepared for your job opening.</p>
    <ul class="ticks">
      <li>Fill Positions Quickly</li>
      <li>Improve productivity and value</li>
    </ul>
  </section>

  <footer class="abs contacts">
    <div class="contact">
      <svg width="18" height="20" viewBox="0 0 24 24"><path d="M6.6 2.5l3 3.2-1.8 2.6c1.2 2.8 3.4 5 6.2 6.3l2.6-1.8 3.2 3-1.6 3.6C11 19 4.9 12.9 3 5.1z" fill="var(--orange)"/></svg>
      <span>5550142387</span>
    </div>
    <div class="contact">
      <svg width="22" height="15" viewBox="0 0 22 15"><rect x="1" y="1" width="20" height="13" fill="none" stroke="var(--orange)" stroke-width="2"/><path d="M1 1l10 7 10-7" fill="none" stroke="var(--orange)" stroke-width="2"/></svg>
      <span>info@lorvantsystems.example</span>
    </div>
    <div class="contact">
      <svg width="14" height="22" viewBox="0 0 14 22"><path d="M7 1a6 6 0 0 0-6 6c0 5 6 14 6 14s6-9 6-14a6 6 0 0 0-6-6z" fill="var(--orange)"/><circle cx="7" cy="7" r="2.3" fill="var(--blue-deep)"/></svg>
      <span>Two Harbor Plaza 410 Fifth<br>Street NW</span>
    </div>
    <div class="contact">
      <svg width="18" height="18" viewBox="0 0 18 18"><circle cx="9" cy="9" r="7.5" fill="none" stroke="var(--orange)" stroke-width="2"/><path d="M1.5 9h15M9 1.5c-3 3.5-3 11.5 0 15M9 1.5c3 3.5 3 11.5 0 15" fill="none" stroke="var(--orange)" stroke-width="1.5"/></svg>
      <span>www.lorvantsystems.example</span>
    </div>
  </footer>
</main>
</body>
</html>
```